High End Business Card Design for Flooring Store

Looking for a new card design for our hardwood flooring company. We have no print budget for these and are open to cards made from wood, metal, cardstock with embossed print ... or any combination of these. No plastic.

We sell luxury products and I want the cards to reflect our image of quality and class.

Our contact information as such;
Employee Name
418 Colbrook Blvd.
Ashbury, ON
K9R-3M5
(555) 214-3968
Employee email @velkaflooring.com

Target Market(s)

Home Builders

Contact Information for Business Card

Emnployee name, business contact information

```html
<!DOCTYPE html>
<html lang="en">
<head>
<meta charset="utf-8">
<title>Velka Flooring — Business Card</title>
<link href="https://fonts.googleapis.com/css2?family=Montserrat:wght@400;500;700;800&display=swap" rel="stylesheet">
<style>
  :root {
    --page: #2a2a2a;
    --card: #161616;
    --brand-red: #a8302b;
    --gold: #e8b526;
    --grey: #5e5e5e;
    --ink: #f2f2f2;
  }
  * { box-sizing: border-box; margin: 0; padding: 0; }
  html, body { width: 1200px; height: 1200px; overflow: hidden; }
  body {
    background: var(--page);
    font-family: "Montserrat", sans-serif;
    display: flex;
    flex-direction: column;
    align-items: center;
    justify-content: center;
    gap: 60px;
  }
  .card {
    width: 840px;
    height: 480px;
    background: var(--card);
    border-radius: 28px;
    position: relative;
    overflow: hidden;
    box-shadow: 0 20px 40px rgba(0,0,0,.45);
  }
  /* back */
  .card-back .emboss-field {
    position: absolute; inset: 0;
    background: linear-gradient(135deg, #1b1b1b 0%, #141414 55%, #1a1a1a 100%);
  }
  .card-back .wordmark {
    position: absolute;
    right: 120px; bottom: 150px;
    display: flex; align-items: center; gap: 14px;
  }
  .brand-square { width: 40px; height: 40px; background: var(--gold); }
  .brand-name {
    font-weight: 500;
    color: var(--brand-red);
    letter-spacing: 1px;
    line-height: 1;
  }
  .card-back .brand-name { font-size: 64px; }
  /* front */
  .card-front .logo-block {
    position: absolute;
    left: 90px; top: 160px;
  }
  .card-front .wordmark { display: flex; align-items: center; gap: 16px; }
  .card-front .brand-square { width: 56px; height: 56px; }
  .card-front .brand-name { font-size: 96px; }
  .tagline {
    margin-top: 10px;
    margin-left: 76px;
    color: var(--grey);
    font-size: 21px;
    line-height: 1.2;
    font-weight: 500;
  }
  .tagline span { display: block; }
  .tagline span + span { padding-left: 30px; }
  .divider {
    position: absolute;
    left: 470px; top: 110px;
    width: 1.5px; height: 250px;
    background: var(--gold);
  }
  .contact {
    position: absolute;
    left: 505px; top: 105px;
    color: var(--ink);
    font-size: 17px;
    line-height: 1.3;
  }
  .employee-name {
    color: var(--gold);
    font-weight: 800;
    font-size: 22px;
    margin-bottom: 18px;
  }
  .contact-row { display: flex; gap: 10px; align-items: flex-start; margin-bottom: 4px; }
  .contact-row svg { width: 16px; height: 16px; flex: none; margin-top: 3px; fill: var(--gold); }
  .address { margin-bottom: 28px; }
</style>
</head>
<body>
  <section class="card card-back">
    <div class="emboss-field" role="img" aria-label="Faint embossed repeating brand name pattern across the card"></div>
    <div class="wordmark">
      <span class="brand-square"></span>
      <span class="brand-name">Velka</span>
    </div>
  </section>

  <section class="card card-front">
    <div class="logo-block">
      <div class="wordmark">
        <span class="brand-square"></span>
        <span class="brand-name">Velka</span>
      </div>
      <p class="tagline"><span>Planchers &amp; Escaliers</span><span>Flooring &amp; Stairs</span></p>
    </div>
    <div class="divider"></div>
    <div class="contact">
      <p class="employee-name">Employee Name</p>
      <div class="contact-row address">
        <svg viewBox="0 0 16 16"><path d="M8 0a5.5 5.5 0 0 0-5.5 5.5C2.5 10 8 16 8 16s5.5-6 5.5-10.5A5.5 5.5 0 0 0 8 0zm0 8a2.5 2.5 0 1 1 0-5 2.5 2.5 0 0 1 0 5z"/></svg>
        <p>418 Colbrook Blvd.<br>Ashbury, ON K9R-3M5</p>
      </div>
      <div class="contact-row">
        <svg viewBox="0 0 16 16"><path d="M3.6 1l2.3 3-1.4 1.8c.9 2 2.6 3.7 4.7 4.7l1.8-1.4 3 2.3-1.5 2.6C7 14 2 9 1 2.5z"/></svg>
        <p>(555) 214-3968</p>
      </div>
      <div class="contact-row">
        <svg viewBox="0 0 16 16"><path d="M1 3h14v10H1zm1.5 1.3v.4L8 8.6l5.5-3.9v-.4z"/></svg>
        <p>email@velkaflooring.com</p>
      </div>
    </div>
  </section>
</body>
</html>
```